Stick and Box Packaging for Coffee

We are looking to have tube and stick designs (packaging) for our coffee product.
Use these two different kinds of packaging for your design references.

1. http://www.plivorant.com/market-we-serve/beverages/coffee
2. http://www.grabomix.com/reclosable-tubes.html

Please include a RED color somewhere on the design. May be a border line or just come up with the design. Please see the attached images as reference.

Estimated Dimension:
1. Height - 0.88 inches
2. Length - 4.50 inches

sample color palettes:
Brown
Black
Red
Green
Golden Brown

*Please make the packaging look like a premium/high end packaging.

For the meantime - please use "Tundra Coffee" as the brand name also make a sample logo for it. For the Nutrifacts and other write up, just use a sample information.

By the way, this product is VERDAmark and FRAB Organic Certified. Please do not add the nutrifacts on the sticks just write it on the box. Make the box the same design as Quelvane cigarette and the color texture a mix of glossy and matte texture.

Please use the images from this link as your additional reference for the stick and box sizes and other information

http://shpq.to/7KuwPmd

Happy New Year and Happy Designing!!!

Target Market(s)

High End and Upscale consumers

Industry/Entity Type

Product

Requirements
Must have
• Sample logo - you can use any logo just for the design then once we have the final logo I will send it to the winner.
• Additional info: Please showcase the Stick design on the box as well like the one from the Coconut Sugar packaging but make some originality with the design on are you going to showcase that on the box
Nice to have
• Please create a sample logo for "Tundra Coffee". This is not the final brand that is why we don't want to create a permanent logo. Just a placeholder Logo will do for now - any - so long as it is relevant - and especially not using known brands.

```html
<!DOCTYPE html>
<html lang="en">
<head>
<meta charset="utf-8">
<title>Tundra Coffee – Stick Label</title>
<link href="https://fonts.googleapis.com/css2?family=Open+Sans:wght@400;600&display=swap" rel="stylesheet">
<style>
  :root {
    --backdrop: #c9c9c9;
    --label-white: #f7f7f6;
    --label-shade: #e4e4e2;
    --brand-red: #b3131b;
    --brand-red-deep: #8e0c12;
    --coffee-dark: #3a1d0c;
    --coffee-mid: #8a4a1c;
    --coffee-light: #c98a4a;
    --text-light: #ffffff;
  }
  html, body {
    margin: 0;
    padding: 0;
    width: 1200px;
    height: 724px;
    overflow: hidden;
    background: var(--backdrop);
    font-family: "Open Sans", Arial, sans-serif;
  }
  .stick-label {
    position: absolute;
    left: 60px;
    top: 256px;
    width: 1080px;
    height: 212px;
    box-shadow: 0 10px 30px rgba(0,0,0,0.18);
  }
  .stick-label svg { display: block; }
  .brand-name {
    font-family: "Open Sans", Arial, sans-serif;
    font-weight: 600;
    fill: var(--brand-red);
  }
  .open-hint {
    font-family: "Open Sans", Arial, sans-serif;
    font-weight: 400;
    fill: var(--text-light);
  }
</style>
</head>
<body>
  <div class="stick-label">
    <svg width="1080" height="212" viewBox="0 0 1080 212">
      <defs>
        <linearGradient id="label-base" x1="0" y1="0" x2="1" y2="1">
          <stop offset="0" stop-color="var(--label-white)"/>
          <stop offset="1" stop-color="var(--label-shade)"/>
        </linearGradient>
        <radialGradient id="splash-tone" cx="0.5" cy="0.5" r="0.55">
          <stop offset="0" stop-color="var(--coffee-mid)"/>
          <stop offset="0.5" stop-color="var(--coffee-light)" stop-opacity="0.7"/>
          <stop offset="1" stop-color="var(--label-white)" stop-opacity="0"/>
        </radialGradient>
        <linearGradient id="bean-tone" x1="0" y1="0" x2="1" y2="1">
          <stop offset="0" stop-color="var(--brand-red)"/>
          <stop offset="1" stop-color="var(--brand-red-deep)"/>
        </linearGradient>
      </defs>

      <rect class="label-base" x="0" y="0" width="1080" height="212" fill="url(#label-base)"/>

      <text class="brand-name" x="60" y="100" font-size="56">Tundra</text>
      <text class="brand-name" x="90" y="160" font-size="56">Coffee</text>

      <ellipse class="splash-area" cx="560" cy="106" rx="200" ry="110" fill="url(#splash-tone)"
               role="img" aria-label="Splash of dark coffee arcing across the label"/>

      <path class="bean-band" d="M730 0 Q700 106 712 212 L1080 212 L1080 0 Z" fill="url(#bean-tone)"
            role="img" aria-label="Red-toned roasted coffee beans backdrop"/>
      <path class="band-edge" d="M748 0 Q718 106 730 212" fill="none" stroke="var(--text-light)" stroke-width="3"/>

      <g class="open-hint" transform="translate(790 20) rotate(90)" font-size="28">
        <text x="0" y="0">band top</text>
        <text x="0" y="-34">towards</text>
        <text x="0" y="-68">you</text>
      </g>
    </svg>
  </div>
</body>
</html>
```